Heritage Hollow Business Cards

Require a business card design. <br/><br/>Needs to include logo (either round or long version) plus these details:<br/>Maya Torvel<br/>Heritage Hollow<br/>maya@quonbrook.com.au<br/>02 6481 7390<br/>PO Box Glenwarra NSW 2913<br/>www.heritagehollow.com.au<br/><br/>I need in an editable format so that I can create for multiple staff members. <br/><br/>

Target Market(s)

We are an online store selling renovation products to home owners are builders. Looking for a classic classy design.

Industry/Entity Type

Home And Garden

Contact Information for Business Card

Maya Torvel
Heritage Hollow
maya@quonbrook.com.au
02 6481 7390
PO Box Glenwarra NSW 2913
www.heritagehollow.com.au

Colors

Designer to choose colors to be used in the design.

Requirements
Must have
• Must include Logo.

```html
<!DOCTYPE html>
<html lang="en">
<head>
<meta charset="utf-8">
<title>Heritage Hollow Business Cards</title>
<link href="https://fonts.googleapis.com/css2?family=Gelasio:wght@400&display=swap" rel="stylesheet">
<style>
  :root {
    --backdrop: #a5a6aa;
    --shadow: #4b4b4e;
    --card-light: #ffffff;
    --card-dark: #231f20;
    --ink: #231f20;
    --ink-light: #ffffff;
  }
  * { margin: 0; padding: 0; box-sizing: border-box; }
  html, body {
    width: 960px; height: 1200px; overflow: hidden;
    background: var(--backdrop);
    font-family: "Gelasio", Georgia, serif;
    color: var(--ink);
  }
  .canvas { position: relative; width: 960px; height: 1200px; }
  .card { position: absolute; left: 60px; width: 840px; height: 480px; }
  .card-shadow {
    position: absolute; left: 24px; top: 24px; width: 100%; height: 100%;
    background: var(--shadow);
    filter: blur(2px);
  }
  .card-face { position: absolute; inset: 0; overflow: hidden; }

  .card-front { top: 120px; }
  .card-front .card-shadow,
  .card-front .card-face { border-radius: 0 56px 0 56px; }
  .card-front .card-face { background: var(--card-light); }

  .brand-mark {
    position: absolute; left: 48px; top: 26px;
    width: 140px; height: 140px;
    border: 1.5px solid var(--ink); border-radius: 50%;
  }
  .brand-name {
    position: absolute; left: 58px; top: 114px;
    font-size: 44px; line-height: 1; white-space: nowrap;
  }
  .person { position: absolute; left: 42px; top: 296px; }
  .person-name { font-size: 35px; line-height: 38px; white-space: nowrap; }
  .person-company { font-size: 18px; line-height: 24px; white-space: nowrap; }
  .divider {
    position: absolute; left: 0; right: 0; top: 364px; height: 3px;
    background: var(--ink);
  }
  .contact-list {
    position: absolute; top: 385px; list-style: none; font-size: 18px;
  }
  .contact-list li {
    display: flex; align-items: center; height: 31px; white-space: nowrap;
  }
  .contact-list svg { width: 15px; height: 15px; margin-right: 17px; flex: none; }
  .contact-left { left: 42px; }
  .contact-right { left: 428px; }

  .card-back { top: 640px; }
  .card-back .card-shadow,
  .card-back .card-face { border-radius: 56px 0 56px 0; }
  .card-back .card-face { background: var(--card-dark); }
  .back-mark {
    position: absolute; left: 276px; top: 90px; width: 316px; height: 316px;
    border: 1px solid var(--ink-light); border-radius: 50%;
  }
  .back-name {
    position: absolute; left: 316px; top: 256px;
    color: var(--ink-light); font-size: 42px; line-height: 40px;
  }
</style>
</head>
<body>
<main class="canvas">
  <section class="card card-front" aria-label="Business card front">
    <div class="card-shadow"></div>
    <div class="card-face">
      <div class="brand-mark"></div>
      <div class="brand-name">Heritage Hollow</div>

      <div class="person">
        <div class="person-name">Maya Torvel</div>
        <div class="person-company">Heritage Hollow</div>
      </div>

      <div class="divider"></div>

      <ul class="contact-list contact-left">
        <li>
          <svg viewBox="0 0 16 16" aria-hidden="true"><path d="M1 6 L8 1 L15 6 V15 H1 Z" fill="#231f20"/><path d="M1 7 L8 11 L15 7" fill="none" stroke="#fff" stroke-width="1.3"/></svg>
          maya@quonbrook.com.au
        </li>
        <li>
          <svg viewBox="0 0 16 16" aria-hidden="true"><rect x="1" y="1" width="14" height="14" rx="3" fill="#231f20"/><path d="M6 4 C4 6 6 11 10 12" fill="none" stroke="#fff" stroke-width="1.4"/></svg>
          02 6481 7390
        </li>
      </ul>
      <ul class="contact-list contact-right">
        <li>
          <svg viewBox="0 0 16 16" aria-hidden="true"><path d="M8 15 C4 10 3 8 3 6 A5 5 0 0 1 13 6 C13 8 12 10 8 15 Z" fill="#231f20"/><circle cx="8" cy="6" r="2" fill="#fff"/></svg>
          PO Box Glenwarra NSW 2913
        </li>
        <li>
          <svg viewBox="0 0 16 16" aria-hidden="true"><g fill="none" stroke="#231f20" stroke-width="1.2"><circle cx="8" cy="8" r="6.5"/><ellipse cx="8" cy="8" rx="3" ry="6.5"/><path d="M1.5 8 H14.5 M3 4.5 H13 M3 11.5 H13"/></g></svg>
          www.heritagehollow.com.au
        </li>
      </ul>
    </div>
  </section>

  <section class="card card-back" aria-label="Business card back">
    <div class="card-shadow"></div>
    <div class="card-face">
      <div class="back-mark"></div>
      <div class="back-name">Heritage<br>Hollow</div>
    </div>
  </section>
</main>
</body>
</html>
```